Motel Sign - Front

(21/03/12 - I've edited the brief and removing the words "garden view" its not fitting in the designs I'm getting and just want the word motel to be the focus. I have a template/vision of what I want - see the whiteboard sketch of what I'm looking for uploaded today. Definitely open to creatively, new designs and different ideas but the whiteboard design I've done should be a guideline. Keep it fresh/green/white. use the sample photos of green as inspiration. Thanks)
We are a motel set in the mountain country of Victoria - Australia. The front of the motel needs a fresh look. We recently removed a large amount of the garden to expose a brick courtyard fence which the front of the courtyard faces out to the main road. Within the courtyard fence there is a wooden frame and paneling.
We want to have a new sign created to slot into the wooden frame. (see photo) its the white component.
Its a very large and unusual shape and I want to keep it simple but need to fill the in the best way possible.
The space is 940mm high and 4940mm width.
The message of the sign is simple the word "MOTEL". I want people to be able to drive past and glance in and see we are a motel straight away. So the main purpose of the sign is to say "MOTEL".
I am open to colour use to match the space and have impact. I thought a background colour should be 'off white'. I'm open to the colours used to match your design as long as it matches the brief. Maybe a garden green for the emblem.
IN BRIEF:
1) the word "MOTEL"
2) Border/Background that ties in the garden.
The design should be centred, clean and simple, doesn't have to fill the whole space as long as its balanced and centred.
I like cursive and garden like designs for this one - as long its the word MOTEL still has impact. (OPEN TO NEW IDEAS)
I am also open to different ideas and suggestions if you feel you have a better way to take advantage of this space.
The sign will be 7-8 metres from the road itself.
NOTE: the photos show the space and the painted white in the space where the sign will go. The garden in front of this space will be completely cleared.
Motel

```html
<!DOCTYPE html>
<html lang="en">
<head>
<meta charset="utf-8">
<title>Motel Sign – Front Concepts</title>
<link rel="stylesheet" href="https://fonts.googleapis.com/css2?family=Bowlby+One&family=Metamorphous&family=Libre+Baskerville:wght@700&display=swap">
<style>
  :root {
    --page: #ffffff;
    --leaf-light: #c9e27a;
    --leaf-mid: #a6cf5c;
    --leaf-deep: #7fba45;
    --sun: #e4ea3c;
    --frond: rgba(255, 255, 255, 0.35);
    --letter: #ffffff;
    --outline: #0f3d14;
    --shadow: #1d4a1a;
    --label: #111111;
  }
  * { margin: 0; padding: 0; box-sizing: border-box; }
  html, body {
    width: 1200px;
    height: 685px;
    overflow: hidden;
    background: var(--page);
  }
  .canvas {
    position: relative;
    width: 1200px;
    height: 685px;
  }
  .sign {
    position: absolute;
    left: 70px;
    width: 1096px;
    height: 210px;
    overflow: hidden;
  }
  .sign--rounded { top: 22px; }
  .sign--nouveau { top: 380px; }
  .sign__garden {
    position: absolute;
    inset: 0;
    background:
      radial-gradient(ellipse 22% 60% at 28% 45%, var(--sun) 0%, transparent 70%),
      radial-gradient(ellipse 18% 55% at 8% 80%, var(--leaf-deep) 0%, transparent 75%),
      radial-gradient(ellipse 18% 55% at 94% 85%, var(--leaf-deep) 0%, transparent 75%),
      linear-gradient(100deg, var(--leaf-mid) 0%, var(--leaf-light) 45%, var(--leaf-mid) 100%);
  }
  .sign__vines {
    position: absolute;
    top: 0;
    width: 150px;
    height: 210px;
  }
  .sign__vines--left {
    left: 0;
    background: radial-gradient(ellipse 70% 60% at 35% 45%, var(--frond) 0%, transparent 75%);
  }
  .sign__vines--right {
    right: 0;
    background: radial-gradient(ellipse 70% 60% at 65% 55%, var(--frond) 0%, transparent 75%);
  }
  .sign__word {
    position: absolute;
    inset: 0;
    display: flex;
    align-items: center;
    justify-content: center;
    color: var(--letter);
    -webkit-text-stroke: 6px var(--outline);
    paint-order: stroke fill;
    line-height: 1;
    white-space: nowrap;
    font-weight: 400;
  }
  .sign--rounded .sign__word {
    font-family: "Bowlby One", sans-serif;
    font-size: 160px;
    letter-spacing: 4px;
    padding-right: 110px;
    text-shadow: 7px 8px 0 var(--shadow);
  }
  .sign--nouveau .sign__word {
    font-family: "Metamorphous", serif;
    font-size: 176px;
    letter-spacing: 6px;
    padding-top: 12px;
    text-shadow: 7px 7px 0 var(--shadow);
  }
  .concept-number {
    position: absolute;
    left: 0;
    width: 1236px;
    text-align: center;
    font-family: "Libre Baskerville", serif;
    font-weight: 700;
    font-size: 27px;
    color: var(--label);
  }
  .concept-number--one { top: 250px; }
  .concept-number--two { top: 607px; }
</style>
</head>
<body>
<main class="canvas">
  <section class="sign sign--rounded">
    <div class="sign__garden" role="img" aria-label="Fresh green garden backdrop with soft swirls"></div>
    <div class="sign__vines sign__vines--left" role="img" aria-label="White fern fronds and curling vines"></div>
    <div class="sign__vines sign__vines--right" role="img" aria-label="White fern fronds and curling vines"></div>
    <h1 class="sign__word">MOTEL</h1>
  </section>
  <p class="concept-number concept-number--one">1</p>

  <section class="sign sign--nouveau">
    <div class="sign__garden" role="img" aria-label="Fresh green garden backdrop with soft swirls"></div>
    <div class="sign__vines sign__vines--left" role="img" aria-label="White fern fronds and curling vines"></div>
    <div class="sign__vines sign__vines--right" role="img" aria-label="White fern fronds and curling vines"></div>
    <h2 class="sign__word">MOTEL</h2>
  </section>
  <p class="concept-number concept-number--two">2</p>
</main>
</body>
</html>
```